Fun but professional website required for school teaching consultancy.

Dear Designers,

I have an interesting brief for you. My client is a skilled teacher who is looking to promote her consultancy that provides bespoke training and support to other teachers.

She would like a website that promotes her philosophy for working with children, which is essentially that she wants to create a fun and creative learning environment for them, whilst maintaining the professionalism that is also required to succeed. Representation of the balance between these two points is crucial to the design.

Typically these kind of websites are pretty boring so we need something fun and vibrant, not uninviting ie those typical images of a teacher sat behind a desk or anything overly formal.

Here is an example of what we do not want: http://www.brightmarlowtutors.co.uk/ - in this one although my client liked the layout, she hated the graphics.

Here is a website that she really liked and captured the vibe of what she is trying to promote about herself: http://www.pennyvalekidsplace.com/ - this design indicates fun with learning, happy kids, lively colours and still has a professional feel as well.

If you have any further questions, please ask

Many thanks,

Gareth

PS Enclosed please find a whole bunch of resources (including site map) for this project. My client has supplied graphics, page content and plenty of visuals so hopefully this will make things easier
Updates

To all designers,

Thanks all your designs. Just to let you all know they have been sent to the client and I will supply feedback to you all individually when I get it.

Many thanks,
Gareth

Hi all,

We've had loads of designs for this project so thanks to you all very much. If there is any feedback to pass on, I will do this directly. Right now, all designs have been liked and are in the running. My client is going through them all and will make a decision on the deadline date which is the 10th May.
If you don't hear from me before then, it's simply because no alterations have been requested.

Many thanks.
Gareth

Industry/Entity Type

Training

```html
<!DOCTYPE html>
<html lang="en">
<head>
<meta charset="utf-8">
<title>Keystone Learning</title>
<link rel="stylesheet" href="https://fonts.googleapis.com/css2?family=Shadows+Into+Light&family=Ubuntu:wght@400;500&display=swap">
<style>
:root{
  --sky-top:#1f9fc0;
  --sky-bottom:#4cc3f6;
  --orange:#f9a100;
  --lime:#9ab81e;
  --red:#dc3514;
  --cyan:#34d8f6;
  --gold:#fbb900;
  --magenta:#e5168f;
  --blue-head:#1196d6;
  --green-head:#2bae0c;
  --green-tab:#52b840;
  --teal:#3fd9b4;
  --panel:#f0f0ea;
  --ink:#1d1d1d;
  --white:#ffffff;
}
*{margin:0;padding:0;box-sizing:border-box}
html,body{width:1200px;height:1067px;overflow:hidden;background:var(--white)}
body{position:relative;font-family:"Ubuntu",sans-serif;color:var(--ink)}
.abs{position:absolute}

.site-header{left:0;top:0;width:1200px;height:177px;background:linear-gradient(var(--sky-top),var(--sky-bottom))}
.top-stripes{left:0;top:0;width:1200px;height:3px;background:linear-gradient(90deg,#e8d65a 0 11%,#9fd0dc 11% 22%,#e9a9c4 22% 33%,#9fd0dc 33% 44%,#e8d65a 44% 55%,#9fd0dc 55% 66%,#e9a9c4 66% 77%,#e8d65a 77% 88%,#9fd0dc 88%)}
.brand{left:189px;top:20px;width:94px;height:136px;background:var(--white);border:2px solid #e8f3fa}
.brand-mark{width:86px;height:94px;background:#7fb4de;position:absolute;top:2px;left:2px}
.brand-name{position:absolute;left:0;top:102px;width:90px;font-size:9px;color:#3c6fae;text-align:center;line-height:12px;font-weight:500}
.call{right:189px;top:17px;font-size:19px;letter-spacing:5px;color:var(--white);opacity:.9}
.email{right:189px;top:40px;font-size:18px;color:var(--white);opacity:.95}
.email span{text-decoration:underline}
.main-nav{left:482px;top:81px;width:529px;height:84px;display:flex}
.main-nav a{flex:1;display:flex;align-items:center;justify-content:center;text-align:center;color:var(--white);font-family:Arial,sans-serif;font-size:12px;line-height:15px;text-decoration:none}

.hero{left:189px;top:202px;width:598px;height:310px;background:radial-gradient(ellipse at 50% 45%,#b8926c 0%,#6e6a3a 40%,#2f4a22 100%)}
.hero-caption{left:0;bottom:0;width:598px;height:63px;background:rgba(30,30,30,.72)}
.hero-text{left:30px;top:20px;font-size:15px;color:var(--white);font-weight:500}
.hero-btn{left:473px;top:16px;width:108px;height:36px;background:var(--teal);border:1px dashed var(--white);outline:1px solid var(--teal);font-family:"Shadows Into Light",cursive;font-size:18px;font-weight:700;display:flex;align-items:center;justify-content:center;color:#103b30}

.sidebar-hours{left:794px;top:201px;width:217px;height:311px;background:var(--red);color:var(--white)}
.hand{font-family:"Shadows Into Light",cursive}
.hours-title{left:30px;top:9px;font-size:21px}
.hours{left:13px;top:48px;font-size:10px;line-height:15.4px;border-collapse:collapse}
.hours td{padding:0}
.hours td:first-child{width:82px}
.divider{left:39px;top:140px;width:140px;border-top:1px dashed rgba(255,255,255,.8)}
.blog-title{left:44px;top:150px;font-size:21px}
.blog-text{left:10px;top:190px;width:200px;font-size:10px;line-height:15.4px}
.read-more{right:18px;top:282px;font-size:14px}
.bubbles{left:789px;top:488px}

.contact{left:795px;top:561px;width:216px;height:246px;background:var(--panel);border-bottom:3px dotted var(--green-tab)}
.contact-tab{left:0;top:0;width:124px;height:37px;background:var(--green-tab);color:var(--white);font-size:16px;font-weight:500;padding:9px 0 0 15px;border-bottom:3px dotted var(--white)}
.contact-body{left:12px;top:60px;font-size:10.5px;line-height:13.5px;width:196px}
.contact-body .label{color:var(--green-head)}
.contact-body p{margin-bottom:8px}

.quote{left:795px;top:845px;width:216px;height:152px;background:var(--panel);border-bottom:3px dotted var(--teal)}
.quote-ghost{left:20px;top:12px;font-size:15px;color:var(--white)}
.quote-mark{font-family:Georgia,serif;font-size:62px;color:#c4c4bd;line-height:1}
.quote-open{left:4px;top:0}
.quote-close{right:10px;top:98px}
.quote-text{left:0;top:55px;width:216px;text-align:center;font-size:16px;line-height:21px;color:#2a2a2a}

.welcome{left:187px;top:546px;width:567px;text-align:center;font-size:30px;font-weight:400;color:var(--blue-head)}
.section-title{left:187px;width:567px;text-align:center;font-size:21px;font-weight:400}
.what{top:611px;color:#d51ec8}
.philosophy{top:787px;color:var(--green-head)}
.copy{left:187px;width:570px;font-size:10.9px;color:var(--ink)}
.copy a{color:#d51ec8;text-decoration:none}
.copy-what{top:648px;line-height:15.4px}
.copy-philosophy{top:823px;line-height:14.6px}

.footer{top:1031px;font-size:9.8px}
.footer-left{left:188px}
.footer-right{right:189px}
</style>
</head>
<body>
<header class="site-header abs">
  <div class="top-stripes abs"></div>
  <div class="brand abs">
    <div class="brand-mark"></div>
    <div class="brand-name">Keystone<br>Learning Ltd.</div>
  </div>
  <div class="call abs">Call us on : 07700 900418</div>
  <div class="email abs">Email: <span>hello@keystonelearning.example</span></div>
  <nav class="main-nav abs">
    <a style="background:var(--orange)">Courses</a>
    <a style="background:var(--lime)">Consultant<br>Biopics</a>
    <a style="background:var(--red)">Yoga</a>
    <a style="background:var(--cyan)">T &amp; L Services</a>
    <a style="background:var(--gold)">Resources</a>
    <a style="background:var(--magenta)">PE Services</a>
  </nav>
</header>

<section class="hero abs" role="img" aria-label="Photo of three children outdoors looking closely at a leaf">
  <div class="hero-caption abs">
    <div class="hero-text abs">Slider text will come here.</div>
    <div class="hero-btn abs">Learn More...</div>
  </div>
</section>

<aside class="sidebar-hours abs">
  <div class="hours-title hand abs">KL Opening Time</div>
  <table class="hours abs">
    <tr><td>Monday</td><td>9.00 am till 3.00pm</td></tr>
    <tr><td>Tuesday</td><td>9.00 am till 3.00pm</td></tr>
    <tr><td>Wednesday</td><td>9.00 am till 3.00pm</td></tr>
    <tr><td>Thrusday</td><td>9.00 am till 3.00pm</td></tr>
    <tr><td>Friday</td><td>9.00 am till 3.00pm</td></tr>
  </table>
  <div class="divider abs"></div>
  <div class="blog-title hand abs">From the Blog</div>
  <p class="blog-text abs">&nbsp;Latest Blog post will show hereLatest Blog post will show hereLatest Blog post will show hereLatest Blog post will show hereLatest Blog post will show hereLatest Blog post will show here</p>
  <div class="read-more hand abs">Read more...</div>
</aside>
<svg class="bubbles abs" width="80" height="52" viewBox="0 0 80 52">
  <circle cx="23" cy="26" r="23" fill="#fff"/>
  <circle cx="23" cy="26" r="20" fill="#e2553a"/>
  <circle cx="62" cy="18" r="16" fill="#fff"/>
  <circle cx="62" cy="18" r="13" fill="#e2553a"/>
</svg>

<h1 class="welcome hand abs">Welcome to Keystone Learning</h1>
<h2 class="section-title what abs">What we Do</h2>
<p class="copy copy-what abs">Keystone Learning specialises in providing bespoke <a>Teaching and Learning</a> and <a>Physical Education</a> support to the primary education sector.&nbsp; We offer a range of training and support methods, including team teaching, INSET, <a>courses,</a> coaching, mentoring, staff meetings and so on.&nbsp; Working with a diverse range of clients, such as individual primary and secondary schools, clusters,&nbsp; Oakfield Borough Council, School Sports Partnerships, collaborations and Sports Coaches, we are committed to providing professional development that has a real impact on school improvement.<a>Our consultants</a> all bring with them a raft of experience in Primary Education, Physical Education and School Improvement, plus the skills to inspire and enthuse teachers.</p>
<h2 class="section-title philosophy abs">Our Philosophy</h2>
<p class="copy copy-philosophy abs">We are passionate about teaching and learning - both ours and yours!&nbsp; We strive to practice what we preach and ensure that all our training and support is personalised for the group or individual that it is created for.&nbsp; We also know that our support is only as good as our own understanding, so we are dedicated to ensuring our own professional development and constantly reviewing and developing our practice.&nbsp; We work in partnership with our clients to design bespoke professional development opportunities, constantly reviewing and developing the support with the client to ensure their requirements are met.</p>

<aside class="contact abs">
  <div class="contact-tab abs">Contact Us:</div>
  <div class="contact-body abs">
    <p><span class="label">Call:</span><br>07700 900418</p>
    <p style="margin-top:14px"><span class="label">Email:</span><br>hello@keystonelearning.example</p>
    <p style="margin-top:14px"><span class="label">Office</span></p>
    <p style="margin-top:12px">Suite 4 Harbour House, 12 Mill Lane, Oakfield, Kent.<br>ME9 2XQ</p>
  </div>
</aside>

<aside class="quote abs">
  <div class="quote-ghost abs">Contact Us:</div>
  <div class="quote-mark quote-open abs">&ldquo;</div>
  <p class="quote-text abs">A teacher explains, a great teacher inspires.</p>
  <div class="quote-mark quote-close abs">&rdquo;</div>
</aside>

<footer>
  <div class="footer footer-left abs">Copyright @ Suite 4 Harbour House, 12 Mill Lane, Oakfield, Kent. ME9 2XQ</div>
  <div class="footer footer-right abs">hello@keystonelearning.example</div>
</footer>
</body>
</html>
```